KVO - Redesign (PSD Files Only)

Requirements for the site:

1. We need our logo recreated, please use the same design and change colors to work on a white background

2. The site is a "Wizard" based site, that takes the customer through the process of creating a unique web presence that suits there needs

3.Colors Needed - Main "Dark Blue" Secondary = "Dark Grey" -Other = "Light Grey and White"

4.We need a CRISP CLEAN DESIGN, simple design

5.Wireframes are a general layout and may be modified by you to enhance the design

6. We want a complete web 5.0 look with big buttons and text boxes

7.The more personality the better

8. Current Site brightmorrowco.example

9.See attachments for wireframes

10. Designer should deliver PSD files, no coding is required

11. The portfolio wireframe, should look like the design of the pixelharbor portfolio template
Updates

KEEP IT SIMPLE.,.....

We like the quillframe scaffold style of designs

```html
<!DOCTYPE html>
<html lang="en">
<head>
<meta charset="utf-8">
<title>KVO – Custom Website Design</title>
<link href="https://fonts.googleapis.com/css2?family=Chewy&family=Patrick+Hand&family=Open+Sans:wght@400;600;700;800&display=swap" rel="stylesheet">
<style>
  :root{
    --navy:#1e2a36;
    --navy-deep:#161f29;
    --ink:#222b33;
    --blue:#1f8fd6;
    --grey-bg:#e9eaeb;
    --grey-mid:#cfd2d4;
    --white:#ffffff;
  }
  *{box-sizing:border-box;margin:0;padding:0}
  html,body{width:900px;height:1200px;overflow:hidden}
  body{font-family:"Open Sans",Arial,sans-serif;color:var(--ink);background:var(--white);position:relative}

  .top-bar{height:42px;background:var(--navy);display:flex;align-items:center;justify-content:space-between;padding:0 88px;color:var(--white)}
  .main-nav{display:flex;font-size:12px;font-weight:700;letter-spacing:.3px}
  .main-nav a{color:var(--white);text-decoration:none;padding:0 9px;border-right:1px solid #6b7885}
  .main-nav a:first-child{padding-left:0}
  .main-nav a:last-child{border-right:none}
  .top-phone{font-size:12px;font-weight:700}

  .hero{position:absolute;top:42px;left:0;width:900px;height:498px;
    background:radial-gradient(ellipse at 50% 20%,#f7f7f7 0%,#e6e7e8 60%,#d9dbdc 100%)}
  .hero-title{position:absolute;top:78px;left:150px;width:600px;text-align:center;white-space:nowrap;font-family:"Chewy","Comic Sans MS",cursive;font-weight:400;font-size:30px;line-height:36px;color:var(--ink);letter-spacing:.3px}
  .hero-title .accent{color:var(--blue)}
  .hero-sub{position:absolute;top:122px;left:205px;width:500px;text-align:center;font-family:"Patrick Hand","Comic Sans MS",cursive;font-size:18px;line-height:21px;color:#2e3740}
  .bubble{position:absolute;border-radius:50%;background:var(--navy);color:var(--white);display:flex;align-items:center;justify-content:center;text-align:center;font-family:"Patrick Hand","Comic Sans MS",cursive;line-height:1.05}
  .bubble-guarantee{left:800px;top:40px;width:84px;height:84px;font-size:12px;padding:10px}
  .bubble-support{left:86px;top:190px;width:104px;height:104px;font-size:16px;padding:14px}
  .bubble-save{left:736px;top:212px;width:108px;height:108px;font-size:16px;padding:16px}

  .brand{position:absolute;top:290px;left:0;width:100%;display:flex;flex-direction:column;align-items:center}
  .brand-mark{display:flex;align-items:center;gap:8px}
  .brand-square{width:14px;height:14px;background:var(--ink)}
  .brand-name{font-weight:800;font-size:44px;color:var(--ink);letter-spacing:2px;line-height:1}
  .brand-tag{font-size:11px;font-weight:700;margin-top:4px;color:var(--ink)}

  .wizard{position:absolute;top:408px;left:268px;width:380px}
  .wizard-step{font-size:10px;font-weight:700;margin-bottom:4px}
  .wizard-row{display:flex;height:32px;box-shadow:0 1px 3px rgba(0,0,0,.25)}
  .wizard-input{flex:1;background:var(--white);border:1px solid var(--grey-mid)}
  .wizard-button{width:128px;background:var(--navy);color:var(--white);font-size:10px;font-weight:700;display:flex;align-items:center;justify-content:center;letter-spacing:.3px}

  .services{position:absolute;top:540px;left:0;width:900px;height:246px;background:var(--navy);display:flex;justify-content:center;gap:22px;padding-top:28px}
  .service{width:160px;color:var(--white)}
  .service-icon{height:70px;display:flex;justify-content:center;align-items:flex-end}
  .service-title{font-size:12px;font-weight:700;text-align:center;margin-top:8px}
  .service-text{font-size:8.5px;line-height:11px;margin-top:3px;color:#d6dde3}
  .service-list{list-style:none;font-size:8.5px;line-height:11px;margin-top:2px;padding-left:14px;color:#d6dde3}
  .service-list li::before{content:"• "}

  .portfolio{position:absolute;top:786px;left:0;width:900px;height:324px;background:var(--grey-bg)}
  .portfolio-title{text-align:center;font-size:26px;font-weight:600;color:#4a5560;margin-top:20px}
  .portfolio-grid{position:absolute;top:78px;left:144px;display:grid;grid-template-columns:repeat(4,138px);gap:14px}
  .thumb{height:90px;border:4px solid var(--white);box-shadow:0 1px 3px rgba(0,0,0,.3)}
  .t1{background:linear-gradient(#3a8fd1,#cfe4f3)}
  .t2{background:linear-gradient(#2d3b45,#8a9aa4)}
  .t3{background:linear-gradient(#1aa3d8,#e7f5fb)}
  .t4{background:linear-gradient(#5aa63c,#e3efd9)}
  .t5{background:linear-gradient(#245c9c,#a9c7e4)}
  .t6{background:linear-gradient(#b8862d,#f1e4c6)}
  .t7{background:linear-gradient(#7a2a2a,#d9b3a4)}
  .t8{background:linear-gradient(#3c4d5c,#c6ced5)}
  .scroll-cue{position:absolute;bottom:12px;left:438px}

  .site-footer{position:absolute;top:1110px;left:0;width:900px;height:90px;background:var(--navy-deep);color:var(--white);padding:14px 124px;display:flex;justify-content:space-between}
  .footer-left{display:flex;flex-direction:column;gap:8px}
  .copyright{font-size:10px}
  .partner-badge{width:70px;height:36px;background:var(--white);border-radius:3px}
  .consult-link{font-size:10px;font-weight:600}
</style>
</head>
<body>
  <header class="top-bar">
    <nav class="main-nav">
      <a href="#">HOME</a><a href="#">ABOUT</a><a href="#">PORTFOLIO</a><a href="#">CONTACT US</a>
    </nav>
    <div class="top-phone">1.800.555.0142</div>
  </header>

  <section class="hero">
    <h1 class="hero-title">Get a custom <span class="accent">Website design</span> in 21 Days or Less!</h1>
    <p class="hero-sub">find out why we're the #1 custom website design marketplace. our network of designers will create 50+ web design samples for you to choose and our marketing experts will pave the way for your success.</p>
    <div class="bubble bubble-guarantee">100% Satisfaction Guarantee</div>
    <div class="bubble bubble-support">24/7 Customer Support</div>
    <div class="bubble bubble-save">Save 100's on Web design</div>

    <div class="brand">
      <div class="brand-mark"><span class="brand-square"></span><span class="brand-name">KVO</span></div>
      <div class="brand-tag">Bright Morrow Co</div>
    </div>

    <div class="wizard">
      <div class="wizard-step">STEP 1</div>
      <div class="wizard-row">
        <div class="wizard-input"></div>
        <div class="wizard-button">START YOUR PROJECT ›</div>
      </div>
    </div>
  </section>

  <section class="services">
    <div class="service">
      <div class="service-icon">
        <svg width="64" height="64" viewBox="0 0 64 64"><circle cx="32" cy="32" r="30" fill="#fff"/><text x="32" y="45" text-anchor="middle" font-family="Open Sans,sans-serif" font-weight="800" font-size="38" fill="#1e2a36">?</text></svg>
      </div>
      <div class="service-title">Why choose KVO?</div>
      <p class="service-text">We are a full service design &amp; marketing company that will handle everything for you</p>
      <ul class="service-list"><li>Dedicated Project Manager</li><li>Single Point Of contact</li><li>Marketing Coaches</li><li>Low cost</li><li>50+ Design Samples for you</li></ul>
    </div>
    <div class="service">
      <div class="service-icon">
        <svg width="74" height="56" viewBox="0 0 74 56"><rect x="10" y="2" width="54" height="36" rx="2" fill="#fff"/><rect x="15" y="7" width="44" height="26" fill="#1e2a36"/><path d="M2 42h70l-5 8H7z" fill="#fff"/></svg>
      </div>
      <div class="service-title">Webservices</div>
      <p class="service-text">We are a full service design &amp; marketing company that will handle everything for you</p>
      <ul class="service-list"><li>Dedicated Project Manager</li><li>Single Point Of contact</li><li>Marketing Coaches</li><li>Low cost</li><li>50+ Design Samples for you</li></ul>
    </div>
    <div class="service">
      <div class="service-icon">
        <svg width="70" height="60" viewBox="0 0 70 60"><rect x="6" y="40" width="10" height="18" fill="#fff"/><rect x="22" y="30" width="10" height="28" fill="#fff"/><rect x="38" y="22" width="10" height="36" fill="#fff"/><rect x="54" y="12" width="10" height="46" fill="#fff"/><path d="M4 30 L26 14 L38 20 L60 4" stroke="#fff" stroke-width="3" fill="none"/><path d="M52 2h10v10" stroke="#fff" stroke-width="3" fill="none"/></svg>
      </div>
      <div class="service-title">Marketing Services</div>
      <p class="service-text">We are a full service design &amp; marketing company that will handle everything for you</p>
      <ul class="service-list"><li>Dedicated Project Manager</li><li>Single Point Of contact</li><li>Marketing Coaches</li><li>Low cost</li><li>50+ Design Samples for you</li></ul>
    </div>
    <div class="service">
      <div class="service-icon">
        <svg width="74" height="62" viewBox="0 0 74 62"><text x="20" y="54" text-anchor="middle" font-family="Open Sans,sans-serif" font-weight="800" font-size="56" fill="#fff">$</text><rect x="42" y="44" width="8" height="16" fill="#fff"/><rect x="53" y="34" width="8" height="26" fill="#fff"/><rect x="64" y="22" width="8" height="38" fill="#fff"/></svg>
      </div>
      <div class="service-title">Why choose KVO?</div>
      <p class="service-text">We are a full service design &amp; marketing company that will handle everything for you</p>
      <ul class="service-list"><li>Dedicated Project Manager</li><li>Single Point Of contact</li><li>Marketing Coaches</li><li>Low cost</li><li>50+ Design Samples for you</li></ul>
    </div>
  </section>

  <section class="portfolio">
    <h2 class="portfolio-title">Portfolio</h2>
    <div class="portfolio-grid">
      <div class="thumb t1" role="img" aria-label="Website design sample screenshot"></div>
      <div class="thumb t2" role="img" aria-label="Website design sample screenshot"></div>
      <div class="thumb t3" role="img" aria-label="Website design sample screenshot"></div>
      <div class="thumb t4" role="img" aria-label="Website design sample screenshot"></div>
      <div class="thumb t5" role="img" aria-label="Website design sample screenshot"></div>
      <div class="thumb t6" role="img" aria-label="Website design sample screenshot"></div>
      <div class="thumb t7" role="img" aria-label="Website design sample screenshot"></div>
      <div class="thumb t8" role="img" aria-label="Website design sample screenshot"></div>
    </div>
    <svg class="scroll-cue" width="24" height="14" viewBox="0 0 24 14"><path d="M3 3 L12 11 L21 3" stroke="#1e2a36" stroke-width="3" fill="none"/></svg>
  </section>

  <footer class="site-footer">
    <div class="footer-left">
      <div class="copyright">Copyright © 2014 Bright Morrow Co - All Rights Reserved</div>
      <div class="partner-badge"></div>
    </div>
    <div class="consult-link">Request Consultation</div>
  </footer>
</body>
</html>
```